Flyer Design

We are a new service called quilvo.co.uk (see website) This is a premium rate £1:50 per sms text advice service. I am a qualified counsellor who already runs a practice see reslandcounselling.uk and have gotten per,it's ion from CALLMERIDIAN and are registered with them for this service. Quite simply they text Q7 followed by a brief description of their personal dilemma/life or relationship concern to 64391 this is received by me and then I text back with a brief piece of guidance and feedback on their issue. So it is a text based counselling/advice service for those who want a day to day life issue dealt with in confidence,quickly and discreetly. I want the flyers to be basic with a basic and easily transferable and identifiable image like the one on my website.

Industry/Entity Type

Counsellor

```html
<!DOCTYPE html>
<html lang="en">
<head>
<meta charset="utf-8">
<title>Quilvo – Flyer</title>
<link rel="stylesheet" href="https://fonts.googleapis.com/css2?family=Lobster&family=Lobster+Two:ital,wght@1,700&display=swap">
<style>
  :root {
    --band-deep: #1cc3e6;
    --band-light: #62f6f1;
    --paper: #ffffff;
    --ink-white: #ffffff;
    --copy-top: #6be8e4;
    --copy-bottom: #2cc0ec;
    --burst-rim: #d6fbf9;
    --burst-top: #5ee3f4;
    --burst-bottom: #1ab4de;
  }
  html, body {
    margin: 0;
    padding: 0;
    width: 1200px;
    height: 850px;
    overflow: hidden;
    background: var(--paper);
  }
  .flyer {
    display: block;
    width: 1200px;
    height: 850px;
  }
  .brand-name {
    font-family: "Lobster", cursive;
    font-size: 124px;
    fill: var(--ink-white);
  }
  .pitch-copy {
    font-family: "Lobster Two", cursive;
    font-style: italic;
    font-weight: 700;
    font-size: 50px;
  }
  .burst-label {
    font-family: "Lobster Two", cursive;
    font-style: italic;
    font-weight: 700;
    font-size: 42px;
    fill: var(--ink-white);
  }
  .web-address {
    font-family: "Lobster", cursive;
    font-size: 58px;
    fill: var(--ink-white);
  }
</style>
</head>
<body>
<svg class="flyer" viewBox="0 0 1200 850" xmlns="http://www.w3.org/2000/svg" role="img" aria-label="Quilvo flyer: text Q7 to 64391 for advice and support">
  <defs>
    <linearGradient id="band-top-fill" x1="0" y1="0" x2="0" y2="1">
      <stop offset="0" stop-color="var(--band-deep)"/>
      <stop offset="1" stop-color="var(--band-light)"/>
    </linearGradient>
    <linearGradient id="band-bottom-fill" x1="0" y1="0" x2="0" y2="1">
      <stop offset="0" stop-color="var(--band-light)"/>
      <stop offset="1" stop-color="var(--band-deep)"/>
    </linearGradient>
    <linearGradient id="copy-fill" x1="0" y1="0" x2="0" y2="1">
      <stop offset="0" stop-color="var(--copy-top)"/>
      <stop offset="1" stop-color="var(--copy-bottom)"/>
    </linearGradient>
    <linearGradient id="burst-fill" x1="0" y1="0" x2="0" y2="1">
      <stop offset="0" stop-color="var(--burst-top)"/>
      <stop offset="1" stop-color="var(--burst-bottom)"/>
    </linearGradient>
    <filter id="soft-shadow" x="-10%" y="-20%" width="120%" height="140%">
      <feDropShadow dx="0" dy="3" stdDeviation="5" flood-color="#000" flood-opacity="0.3"/>
    </filter>
    <rect id="burst-outer-square" x="-103" y="-103" width="206" height="206"/>
    <rect id="burst-inner-square" x="-90" y="-90" width="180" height="180"/>
  </defs>

  <!-- top band -->
  <polygon class="band band-top" points="0,0 1200,0 1200,158 0,237" fill="url(#band-top-fill)" filter="url(#soft-shadow)"/>
  <!-- bottom band -->
  <polygon class="band band-bottom" points="0,762 1200,686 1200,850 0,850" fill="url(#band-bottom-fill)" filter="url(#soft-shadow)"/>

  <text class="brand-name" x="565" y="178" text-anchor="middle">Quilvo</text>

  <!-- pitch copy -->
  <g class="pitch-copy" fill="url(#copy-fill)" transform="rotate(-3.6 80 370)">
    <text x="80" y="370">Is today just not your day?</text>
    <text x="86" y="428">Text Q7 to 64391 with</text>
    <text x="100" y="490">your problems and a</text>
    <text x="100" y="550">professional will give you</text>
    <text x="104" y="610">advice and support.</text>
  </g>

  <!-- starburst call-out -->
  <g class="burst" transform="translate(955 432)">
    <g class="burst-rim" fill="var(--burst-rim)">
      <use href="#burst-outer-square" transform="rotate(0)"/>
      <use href="#burst-outer-square" transform="rotate(9)"/>
      <use href="#burst-outer-square" transform="rotate(18)"/>
      <use href="#burst-outer-square" transform="rotate(27)"/>
      <use href="#burst-outer-square" transform="rotate(36)"/>
      <use href="#burst-outer-square" transform="rotate(45)"/>
      <use href="#burst-outer-square" transform="rotate(54)"/>
      <use href="#burst-outer-square" transform="rotate(63)"/>
      <use href="#burst-outer-square" transform="rotate(72)"/>
      <use href="#burst-outer-square" transform="rotate(81)"/>
    </g>
    <g class="burst-core" fill="url(#burst-fill)" filter="url(#soft-shadow)">
      <use href="#burst-inner-square" transform="rotate(4.5)"/>
      <use href="#burst-inner-square" transform="rotate(13.5)"/>
      <use href="#burst-inner-square" transform="rotate(22.5)"/>
      <use href="#burst-inner-square" transform="rotate(31.5)"/>
      <use href="#burst-inner-square" transform="rotate(40.5)"/>
      <use href="#burst-inner-square" transform="rotate(49.5)"/>
      <use href="#burst-inner-square" transform="rotate(58.5)"/>
      <use href="#burst-inner-square" transform="rotate(67.5)"/>
      <use href="#burst-inner-square" transform="rotate(76.5)"/>
      <use href="#burst-inner-square" transform="rotate(85.5)"/>
    </g>
    <g class="burst-label" text-anchor="middle">
      <text x="0" y="-82">Text</text>
      <text x="0" y="-26">Q7</text>
      <text x="0" y="30">to</text>
      <text x="0" y="88">64391</text>
    </g>
  </g>

  <text class="web-address" x="1130" y="806" text-anchor="end">quilvo.co.uk</text>
</svg>
</body>
</html>
```